Ad design for a macarons brand

We are a dessert brand with one product line: macarons. Our products delight. Every bite is a dream!

We are launching a new product and would like to lunch a small tactical campaign for the product to boost sales.

The new macron is mango ganache and the middle a mix of sour mango and yuzu (https://www.plumvarell.com/about-the-fruit-584302).

Here are some images we took of the new macaron
https://www.fennlocker.com/sh/qrtwpzhkvbmls/AAFJtRWD-nxPlkhQZ7CeW4DLp?dl=0

I attach the brand guideline document.

Required sizes

1080 x 1350
1080 x 1920

```html
<!DOCTYPE html>
<html lang="en">
<head>
<meta charset="utf-8">
<title>Merelle — Taste the Sunshine</title>
<link rel="stylesheet" href="https://fonts.googleapis.com/css2?family=Playfair+Display:wght@400;800&display=swap">
<style>
  :root {
    --mango-yellow: #F9B934;
    --cream-white: #FFFFFF;
    --soft-white: rgba(255, 255, 255, 0.42);
    --logo-gold: #B7794A;
    --photo-light: #F4D9A0;
    --photo-mid: #EFA642;
    --photo-deep: #D97E2A;
  }
  html, body {
    margin: 0;
    padding: 0;
    overflow: hidden;
  }
  .ad-canvas {
    position: relative;
    width: 675px;
    height: 1200px;
    background: var(--mango-yellow);
    overflow: hidden;
  }
  .slogan-pattern {
    position: absolute;
    inset: 0;
    width: 675px;
    height: 1200px;
  }
  .slogan-row {
    font-family: 'Playfair Display', serif;
    font-size: 57px;
    font-weight: 800;
  }
  .slogan-row--bright {
    fill: var(--cream-white);
  }
  .slogan-row--soft {
    fill: var(--soft-white);
  }
  .product-photo {
    position: absolute;
    left: 88px;
    top: 367px;
    width: 499px;
    height: 374px;
    background:
      radial-gradient(ellipse at 60% 15%, #F6CB3C 0%, transparent 45%),
      radial-gradient(ellipse at 50% 75%, var(--photo-mid) 0%, transparent 65%),
      linear-gradient(160deg, var(--photo-light) 0%, var(--photo-mid) 55%, var(--photo-deep) 100%);
  }
  .brand-card {
    position: absolute;
    left: 249px;
    top: 509px;
    width: 177px;
    height: 89px;
    background: var(--cream-white);
    display: flex;
    align-items: center;
    justify-content: center;
  }
  .brand-name {
    font-family: 'Playfair Display', serif;
    font-weight: 400;
    font-size: 30px;
    letter-spacing: 1px;
    color: var(--logo-gold);
    text-transform: uppercase;
  }
</style>
</head>
<body>
<main class="ad-canvas">
  <svg class="slogan-pattern" viewBox="0 0 675 1200" aria-label="Taste the sunshine, repeated">
    <text class="slogan-row slogan-row--soft" x="12" y="55" textLength="650" lengthAdjust="spacingAndGlyphs">TASTE THE SUNSHINE</text>
    <text class="slogan-row slogan-row--bright" x="12" y="112" textLength="650" lengthAdjust="spacingAndGlyphs">TASTE THE SUNSHINE</text>
    <text class="slogan-row slogan-row--soft" x="12" y="169" textLength="650" lengthAdjust="spacingAndGlyphs">TASTE THE SUNSHINE</text>
    <text class="slogan-row slogan-row--bright" x="12" y="225" textLength="650" lengthAdjust="spacingAndGlyphs">TASTE THE SUNSHINE</text>
    <text class="slogan-row slogan-row--soft" x="12" y="282" textLength="650" lengthAdjust="spacingAndGlyphs">TASTE THE SUNSHINE</text>
    <text class="slogan-row slogan-row--bright" x="12" y="339" textLength="650" lengthAdjust="spacingAndGlyphs">TASTE THE SUNSHINE</text>
    <text class="slogan-row slogan-row--soft" x="12" y="396" textLength="650" lengthAdjust="spacingAndGlyphs">TASTE THE SUNSHINE</text>
    <text class="slogan-row slogan-row--bright" x="12" y="452" textLength="650" lengthAdjust="spacingAndGlyphs">TASTE THE SUNSHINE</text>
    <text class="slogan-row slogan-row--soft" x="12" y="509" textLength="650" lengthAdjust="spacingAndGlyphs">TASTE THE SUNSHINE</text>
    <text class="slogan-row slogan-row--bright" x="12" y="566" textLength="650" lengthAdjust="spacingAndGlyphs">TASTE THE SUNSHINE</text>
    <text class="slogan-row slogan-row--soft" x="12" y="623" textLength="650" lengthAdjust="spacingAndGlyphs">TASTE THE SUNSHINE</text>
    <text class="slogan-row slogan-row--bright" x="12" y="680" textLength="650" lengthAdjust="spacingAndGlyphs">TASTE THE SUNSHINE</text>
    <text class="slogan-row slogan-row--soft" x="12" y="736" textLength="650" lengthAdjust="spacingAndGlyphs">TASTE THE SUNSHINE</text>
    <text class="slogan-row slogan-row--bright" x="12" y="793" textLength="650" lengthAdjust="spacingAndGlyphs">TASTE THE SUNSHINE</text>
    <text class="slogan-row slogan-row--soft" x="12" y="850" textLength="650" lengthAdjust="spacingAndGlyphs">TASTE THE SUNSHINE</text>
    <text class="slogan-row slogan-row--bright" x="12" y="907" textLength="650" lengthAdjust="spacingAndGlyphs">TASTE THE SUNSHINE</text>
    <text class="slogan-row slogan-row--soft" x="12" y="963" textLength="650" lengthAdjust="spacingAndGlyphs">TASTE THE SUNSHINE</text>
    <text class="slogan-row slogan-row--bright" x="12" y="1020" textLength="650" lengthAdjust="spacingAndGlyphs">TASTE THE SUNSHINE</text>
    <text class="slogan-row slogan-row--soft" x="12" y="1077" textLength="650" lengthAdjust="spacingAndGlyphs">TASTE THE SUNSHINE</text>
    <text class="slogan-row slogan-row--bright" x="12" y="1134" textLength="650" lengthAdjust="spacingAndGlyphs">TASTE THE SUNSHINE</text>
    <text class="slogan-row slogan-row--soft" x="12" y="1191" textLength="650" lengthAdjust="spacingAndGlyphs">TASTE THE SUNSHINE</text>
  </svg>

  <div class="product-photo" role="img" aria-label="Photo of mango and yuzu macarons on white paper with fresh mangoes behind"></div>

  <div class="brand-card">
    <span class="brand-name">Merelle</span>
  </div>
</main>
</body>
</html>
```